Christian Motorcycle club/ministry website

I need a website for my Christian Motorcycle Club/Ministry.

This will be a place for members to go, to reach out to the public, to post events, maybe a place to sell support items but not right now

The name of the club is Iron Wardens. I have a logo that I will provide that needs to be on the webpage.

No sport bikes pictures, only cruisers if any images are used.

We are similar to a regular bike club but our mission is to tell other bikers and people about God.

We should have a contact page as well as an online application form.

I would like it to have a tough look to it. Just because we're Christians we're still bikers.

No scantily dressed women pictures

I'm open to any ideas as I don't really know what it should look like so feel free to be very creative.
Updates

Should also have a page for club rules and by laws

This website is for a Motorcycle Club - like the Gravel Kings or The Drifters or The Vandors or Kin of Thunder television show

We are Christians so we tell people about God but we ride big Motorcycles

We wear leather jackets and beards and are tough big guys with tattoos

Here are some links to show you ideas of what kind of webpage we want:
http://www.pirelvo.com/brent/motorcycle/
http://www.layoutvexa.com/demo/58214.html
http://dranmowstudio.com/portfolio/SteadyWolves/index.html
http://gravelkingsquillbycentral.com/index.html
http://www.layoutvexa.com/flash-templates/4918.html
http://www.layoutvexa.com/flash-templates/2853.html
http://www.brizonpage-layouts.com/472905163-Biker-club-Flash-template-website.html

Thank you all for you submissions, you are all very talented artists and did a great job!

I wish you all the best of luck,
Dale

Industry/Entity Type

Club

Requirements
Must have
• Our logo
Should not have
• undressed women, no sport bikes

```html
<!DOCTYPE html>
<html lang="en">
<head>
<meta charset="utf-8">
<title>Iron Wardens Motorcycle Ministry</title>
<link href="https://fonts.googleapis.com/css2?family=Jost:wght@400;500;600;700&family=Arimo:wght@400;700&family=Lilita+One&display=swap" rel="stylesheet">
<style>
  :root {
    --bg-dark: #120c07;
    --bg-warm: #3a2a19;
    --black: #000000;
    --flame-yellow: #f7d23a;
    --flame-orange: #f28a2a;
    --flame-red: #e8262a;
    --title-yellow: #f5cc22;
    --mustard: #e0b92a;
    --white: #ffffff;
    --heading: #3e4a45;
    --body: #222222;
    --link: #a0301a;
    --button: #d9471e;
    --field-border: #8c8c8c;
    --placeholder: #9a9a9a;
    --footer-text: #e8e8e8;
  }
  * { box-sizing: border-box; margin: 0; padding: 0; }
  html, body { width: 1200px; height: 756px; overflow: hidden; }
  body {
    position: relative;
    background: radial-gradient(ellipse at 50% 40%, var(--bg-warm) 0%, #22170d 55%, var(--bg-dark) 100%);
    font-family: "Arimo", Arial, sans-serif;
  }
  .page { position: absolute; left: 171px; top: 0; width: 858px; }

  .site-header { position: relative; height: 203px; }
  .brand {
    position: absolute; left: 0; top: 0; width: 188px; height: 203px;
    background: var(--black);
    display: flex; flex-direction: column; align-items: center; justify-content: center; gap: 12px;
  }
  .brand-mark { width: 54px; height: 54px; border-radius: 50%; background: var(--flame-red); }
  .brand-name {
    font-family: "Jost", sans-serif; font-weight: 700; font-size: 20px;
    color: var(--title-yellow); text-transform: uppercase; letter-spacing: 1px; text-align: center; line-height: 1.15;
  }
  .site-title {
    position: absolute; left: 210px; top: 16px;
    font-family: "Lilita One", "Jost", sans-serif; font-size: 60px; font-weight: 400;
    color: var(--title-yellow); letter-spacing: 1px;
  }
  .flame-band {
    position: absolute; left: 188px; top: 81px; width: 670px; height: 62px;
    background: linear-gradient(to bottom, rgba(247,210,58,0) 0%, var(--flame-yellow) 30%, var(--flame-orange) 65%, var(--flame-red) 100%);
  }
  .nav-bar { position: absolute; left: 188px; top: 143px; width: 670px; height: 60px; background: var(--flame-red); }
  .main-nav a {
    position: absolute; top: 17px;
    font-family: "Jost", sans-serif; font-weight: 700; font-size: 16px;
    color: var(--white); text-decoration: none; letter-spacing: 0.3px;
  }

  .welcome { height: 106px; background: var(--mustard); padding: 14px 40px 0 41px; }
  .welcome h1 { font-family: "Jost", sans-serif; font-weight: 400; font-size: 28px; color: var(--black); line-height: 1.1; }
  .welcome p { margin-top: 4px; font-size: 11px; line-height: 15.4px; color: var(--black); width: 780px; }

  .content { position: relative; height: 379px; background: var(--white); }
  .feature-bike {
    position: absolute; left: 400px; top: 78px; width: 450px; height: 280px; z-index: 0;
    background: radial-gradient(ellipse at 60% 60%, #6d6d6d 0%, #b5b5b5 35%, #ededed 65%, var(--white) 100%);
  }
  .section-title { position: absolute; z-index: 1; left: 48px; font-family: "Jost", sans-serif; font-weight: 500; font-size: 19px; color: var(--heading); }
  .events-title { top: 23px; }
  .events-text { position: absolute; z-index: 1; left: 48px; top: 52px; width: 320px; font-size: 12px; line-height: 19px; color: var(--body); }
  .event-date { position: absolute; z-index: 1; left: 46px; top: 131px; font-size: 11.5px; font-weight: 700; color: var(--body); letter-spacing: 0.3px; }
  .learn-more { position: absolute; z-index: 1; left: 46px; top: 155px; font-size: 11px; font-weight: 700; color: var(--link); text-decoration: none; letter-spacing: 0.4px; }
  .mailing-title { top: 202px; }
  .field {
    position: absolute; z-index: 1; left: 50px; width: 163px; height: 31px;
    border: 1px solid var(--field-border); background: var(--white);
    font-family: "Arimo", Arial, sans-serif; font-size: 11.5px; padding: 0 12px; color: var(--body);
  }
  .field::placeholder { color: var(--placeholder); }
  .field-name { top: 241px; }
  .field-email { top: 280px; }
  .submit {
    position: absolute; z-index: 1; left: 48px; top: 325px; width: 94px; height: 31px;
    background: var(--button); border: none; border-radius: 2px;
    font-family: "Jost", sans-serif; font-weight: 600; font-size: 15px; color: var(--white);
  }

  .site-footer { position: absolute; left: 0; top: 711px; width: 1200px; text-align: center; font-size: 9.5px; color: var(--footer-text); }
</style>
</head>
<body>
  <div class="page">
    <header class="site-header">
      <div class="brand">
        <span class="brand-mark"></span>
        <span class="brand-name">Iron Wardens</span>
      </div>
      <div class="site-title">Iron Wardens</div>
      <div class="flame-band" role="img" aria-label="Row of yellow and red flames across the header"></div>
      <div class="nav-bar">
        <nav class="main-nav">
          <a href="#" style="left:130px">HOME</a>
          <a href="#" style="left:217px">EVENTS</a>
          <a href="#" style="left:315px">PHOTOS</a>
          <a href="#" style="left:418px">MEMBERS</a>
          <a href="#" style="left:532px">GUESTBOOK</a>
        </nav>
      </div>
    </header>

    <section class="welcome">
      <h1>Welcome</h1>
      <p>Lorem ipsum dolor sit amet, consectetuer adipiscing elit. Nam cursus. Morbi ut mi. Nullam enim leo, egestas id, condimentum at, laoreet mattis, massa. Sed eleifend nonummy diam. Praesent mauris ante, elementum et, bibendum at, posuere sit amet, nibh. Duis tincidunt lectus quis dui viverra vestibulum. Suspendisse vulputate aliquam dui. Nulla elementum dui ut augue. Aliquam vehicula mi at mauris.</p>
    </section>

    <main class="content">
      <div class="feature-bike" role="img" aria-label="Chrome custom cruiser motorcycle on a white backdrop"></div>

      <h2 class="section-title events-title">Latest Events</h2>
      <p class="events-text">Pellentesque habitant morbi tristique senectus et netus et malesuada fames ac turpis egestas. In posuere felis nec tortor.</p>
      <div class="event-date">September 10, 2013</div>
      <a class="learn-more" href="#">Learn more</a>

      <h2 class="section-title mailing-title">Join the mailing list</h2>
      <input class="field field-name" type="text" placeholder="Name">
      <input class="field field-email" type="email" placeholder="Email">
      <button class="submit" type="button">Submit</button>
    </main>
  </div>

  <footer class="site-footer">© 2013 Northfield Trade Co. All Rights Reserved</footer>
</body>
</html>
```